Order Management User Interface

I need a new design for our order management screens. They need to be end user friendly and contain the data in an easy to read format. These are online orders. I have attached 3 images from the development solution. For now I just need a new UI and ideally would like it delivered in html so we can easily adapt. The screen has multiple tabs to display the different types of data we store. Ideally the end user needs to see customer focused information first.
I have uploaded an example of a different order view that i like.
Industry/Entity Type
Fashion Retail
Coding
Coded - Design and coding required
Number of Pages Required
1 page

```html
<!DOCTYPE html>
<html lang="en">
<head>
<meta charset="utf-8">
<title>Order Management – Development</title>
<link href="https://fonts.googleapis.com/css2?family=Lato:wght@400;700;900&family=Montserrat:wght@500;600&display=swap" rel="stylesheet">
<style>
:root{
  --bg:#c9cacd;
  --purple:#5a44d6;
  --purple-deep:#4a36c4;
  --teal:#33c4c4;
  --label:#3f58c0;
  --ink:#222430;
  --muted:#555a66;
  --field:#eeeff3;
  --line:#e4e5ea;
  --head:#eeeff2;
  --row-lav:#e6e6f8;
  --row-cyan:#d4f2f2;
  --red:#e84a4a;
  --blue:#2f6fe0;
  --green:#5cc23a;
  --aqua:#39bcc0;
  --white:#ffffff;
}
*{box-sizing:border-box;margin:0;padding:0}
html,body{width:1200px;height:2538px;overflow:hidden;background:var(--bg)}
body{font-family:'Lato',sans-serif;color:var(--ink)}
.stage{position:absolute;left:0;top:0;width:1218px;height:2576px;transform:scale(0.98522);transform-origin:0 0;background:var(--bg)}
.screen{position:absolute;left:100px;width:1017px;height:731px;background:var(--white);overflow:hidden;box-shadow:0 2px 10px rgba(0,0,0,.12)}
.screen--modal{top:104px}
.screen--items{top:922px}
.screen--addresses{top:1740px}

/* sidebar */
.side{position:absolute;left:0;top:0;width:118px;height:100%;background:var(--purple)}
.brand{position:absolute;left:18px;top:13px;font-family:'Montserrat',sans-serif;font-weight:500;font-size:13px;line-height:16px;color:var(--white)}
.menu{list-style:none;position:absolute;left:12px;top:74px;width:106px}
.menu li{height:26px;margin-bottom:11px;display:flex;align-items:center;padding-left:14px;font-size:9.5px;color:var(--white);border-radius:13px 0 0 13px}
.menu li.on{background:var(--white);color:var(--purple)}
.menu .ic{width:8px;height:8px;margin-right:13px;flex:none;fill:currentColor}

/* header */
.title{position:absolute;left:142px;top:14px;font-family:'Montserrat',sans-serif;font-weight:600;font-size:21px;color:var(--ink)}
.search{position:absolute;left:570px;top:11px;width:305px;height:37px;border:1px solid #c8cad0;border-radius:19px;display:flex;align-items:center;padding-left:20px;font-size:8.5px;color:#555}
.search svg{width:8px;height:8px;margin-right:4px}
.hicon{position:absolute;top:24px;width:9px;height:9px;fill:#333}
.hicon--mail{left:899px}
.hicon--bell{left:925px}
.avatar{position:absolute;left:952px;top:11px;width:34px;height:34px;border-radius:50%;background:radial-gradient(circle at 50% 40%,#b08a74,#4d4038);border:2px solid #ddd}
.hrule{position:absolute;left:118px;right:0;top:66px;height:1px;background:var(--line)}

/* sub tabs */
.pill{position:absolute;left:138px;top:77px;width:88px;height:24px;border-radius:4px;background:var(--purple);color:var(--white);font-size:8.5px;display:flex;align-items:center;padding-left:10px}
.pill svg,.crumb svg{width:8px;height:8px;margin-left:5px}
.crumb{position:absolute;left:253px;top:83px;font-size:8.5px;color:var(--label);display:flex;align-items:center}

/* cards */
.card{position:absolute;top:110px;width:196px;height:175px;background:var(--white);border-top:3px solid;border-radius:3px;box-shadow:0 1px 5px rgba(0,0,0,.14)}
.card--a{left:140px;border-color:var(--red)}
.card--b{left:358px;border-color:var(--blue)}
.card--c{left:577px;border-color:var(--green)}
.card--d{left:795px;border-color:var(--aqua)}
.field{position:absolute;left:12px;display:flex;align-items:center;height:23px}
.field:nth-child(1){top:10px}.field:nth-child(2){top:42px}.field:nth-child(3){top:74px}.field:nth-child(4){top:106px}.field:nth-child(5){top:138px}
.field label{width:88px;font-size:8.5px;color:var(--label)}
.box{width:92px;height:23px;background:var(--field);border-radius:4px;font-size:7.5px;color:#333;display:flex;align-items:center;justify-content:space-between;padding:0 8px 0 10px}
.box--lg{font-size:9.5px}
.box--sm{font-size:7px;padding-left:10px;padding-right:3px}
.spin{width:5px;height:8px;fill:#333}

/* tab bar */
.tabs{position:absolute;left:143px;top:300px;display:flex;gap:2px}
.tab{width:79px;height:28px;background:var(--teal);color:var(--white);font-size:10.5px;display:flex;align-items:center;justify-content:center}
.tab.on{background:var(--purple)}

/* items table */
.grid{position:absolute;left:143px;top:332px;width:851px}
.grid .tr{display:grid;grid-template-columns:79px 83px 82px 98px 64px 73px 62px 64px 56px 69px 58px 63px}
.grid .th{height:36px;background:var(--head);font-size:10.5px}
.grid .th>div{display:flex;align-items:center;padding-left:8px}
.grid .th>div:first-child{padding-left:17px}
.grid .th .span2{grid-column:span 2}
.grid .td{height:117px;font-size:7.5px}
.grid .td>div{display:flex;align-items:center;padding-left:8px;border-right:1px solid var(--line)}
.grid .td>div:first-child{padding-left:17px;font-size:8px}
.grid .td>div:last-child{border-right:none}
.grid .td.alt{background:var(--row-cyan)}
.spec{flex-direction:column;align-items:flex-start!important;justify-content:center;line-height:13px;font-weight:700}
.spec--val{color:var(--purple);font-weight:700;padding-left:13px!important}

/* address table */
.atable{position:absolute;left:143px;top:332px;width:851px}
.arow{position:relative;height:36px;font-size:10.5px}
.arow span{position:absolute;top:50%;transform:translateY(-50%)}
.arow--head{background:var(--head)}
.arow--lav{background:var(--row-lav);margin-top:1px}
.arow--cyan{background:var(--row-cyan);margin-top:1px}
.c1{left:17px}.c2{left:134px}.c3{left:238px}.c4{left:369px}.c5{left:495px}.c6{left:614px}.c7{left:731px}

/* modal */
.dim{position:absolute;inset:0;background:rgba(18,16,40,.52)}
.modal{position:absolute;left:260px;top:82px;width:498px;height:568px;background:var(--white);border-radius:20px;overflow:hidden}
.modal-head{height:62px;background:var(--teal);display:flex;align-items:center;justify-content:space-between;padding:0 30px 0 27px;color:var(--white);font-family:'Montserrat',sans-serif;font-weight:600;font-size:17px}
.modal-head svg{width:16px;height:16px}
.form{position:absolute;left:28px;top:80px}
.frow{display:flex;align-items:center;height:28px;margin-bottom:9px}
.frow label{width:76px;font-size:9.5px;color:var(--muted)}
.frow .colon{width:21px;font-size:9.5px;color:var(--muted)}
.frow .input{width:345px;height:28px;border:1px solid #a9acb4;border-radius:2px;font-size:8px;color:#333;display:flex;align-items:center;padding-left:12px}
.actions{position:absolute;left:180px;top:525px;display:flex;gap:9px}
.btn{width:65px;height:22px;border-radius:11px;color:var(--white);font-size:8px;font-weight:700;display:flex;align-items:center;justify-content:center}
.btn--update{background:var(--purple)}
.btn--cancel{background:var(--teal)}
</style>
</head>
<body>
<div class="stage">

<!-- Screen: Address edit dialog -->
<section class="screen screen--modal">
  <nav class="side">
    <div class="brand">Order<br>Management</div>
    <ul class="menu">
      <li class="on"><svg class="ic" viewBox="0 0 10 10"><rect x="0" y="1" width="10" height="8" rx="1"/></svg>Dashboard</li>
      <li><svg class="ic" viewBox="0 0 10 10"><circle cx="3" cy="3" r="2"/><circle cx="7" cy="3" r="2"/><rect x="0" y="6" width="10" height="4" rx="2"/></svg>Teams</li>
      <li><svg class="ic" viewBox="0 0 10 10"><path d="M0 1h2l1.5 5h5L10 2.5H3"/><circle cx="4" cy="8.5" r="1"/><circle cx="8" cy="8.5" r="1"/></svg>Cart</li>
      <li><svg class="ic" viewBox="0 0 10 10"><path d="M5 0a3.5 3.5 0 0 1 3.5 3.5C8.5 6 5 10 5 10S1.5 6 1.5 3.5A3.5 3.5 0 0 1 5 0z"/></svg>Location</li>
      <li><svg class="ic" viewBox="0 0 10 10"><ellipse cx="5" cy="5" rx="5" ry="3"/></svg>View</li>
      <li><svg class="ic" viewBox="0 0 10 10"><path d="M5 0l5 5-5 5-5-5z"/></svg>Countries</li>
      <li><svg class="ic" viewBox="0 0 10 10"><circle cx="5" cy="5" r="5"/></svg>Matches</li>
      <li><svg class="ic" viewBox="0 0 10 10"><circle cx="5" cy="5" r="5"/></svg>Questions</li>
      <li><svg class="ic" viewBox="0 0 10 10"><rect x="0" y="1" width="10" height="8" rx="1"/></svg>View Result</li>
      <li><svg class="ic" viewBox="0 0 10 10"><circle cx="5" cy="5" r="4"/></svg>Settings</li>
      <li><svg class="ic" viewBox="0 0 10 10"><path d="M0 4h6V1l4 4-4 4V6H0z"/></svg>Logout</li>
    </ul>
  </nav>
  <h1 class="title">Development</h1>
  <div class="search"><svg viewBox="0 0 10 10"><circle cx="4" cy="4" r="3" fill="none" stroke="#333" stroke-width="1.6"/><path d="M6 6l3 3" stroke="#333" stroke-width="1.6"/></svg>Search...</div>
  <svg class="hicon hicon--mail" viewBox="0 0 10 10"><rect y="1.5" width="10" height="7"/><path d="M0 1.5l5 4 5-4" fill="none" stroke="#fff" stroke-width="1"/></svg>
  <svg class="hicon hicon--bell" viewBox="0 0 10 10"><path d="M5 0.5a3 3 0 0 1 3 3V7l1.5 1.5h-9L2 7V3.5a3 3 0 0 1 3-3z"/><circle cx="5" cy="9.3" r="0.9"/></svg>
  <div class="avatar" role="img" aria-label="User profile photo"></div>
  <div class="hrule"></div>
  <div class="pill">Order Search <svg viewBox="0 0 10 10"><circle cx="5" cy="5" r="5" fill="#fff"/><path d="M3 3l4 4M7 3l-4 4" stroke="#5a44d6" stroke-width="1.4"/></svg></div>
  <div class="crumb">Order 9670363 <svg viewBox="0 0 10 10"><circle cx="5" cy="5" r="4" fill="none" stroke="#3f58c0" stroke-width="2"/></svg></div>

  <div class="card card--a">
    <div class="field"><label>Order No</label><div class="box">9670363</div></div>
    <div class="field"><label>Orig Order No</label><div class="box">9670363</div></div>
    <div class="field"><label>Customer No</label><div class="box"></div></div>
    <div class="field"><label>Total Retail</label><div class="box">102.00<svg class="spin" viewBox="0 0 5 8"><path d="M0 3.2L2.5 0 5 3.2zM0 4.8L2.5 8 5 4.8z"/></svg></div></div>
    <div class="field"><label>Instructions</label><div class="box"></div></div>
  </div>
  <div class="card card--b">
    <div class="field"><label>Brand</label><div class="box"></div></div>
    <div class="field"><label>Reference</label><div class="box">9670363</div></div>
    <div class="field"><label>First name</label><div class="box">Test</div></div>
    <div class="field"><label>Total Tax</label><div class="box">9.55<svg class="spin" viewBox="0 0 5 8"><path d="M0 3.2L2.5 0 5 3.2zM0 4.8L2.5 8 5 4.8z"/></svg></div></div>
    <div class="field"><label></label><div class="box"></div></div>
  </div>
  <div class="card card--c">
    <div class="field"><label>Order Type</label><div class="box">Sale</div></div>
    <div class="field"><label>Order Channel</label><div class="box">Standard</div></div>
    <div class="field"><label>Surname</label><div class="box">Order</div></div>
    <div class="field"><label>Shipping Amount</label><div class="box">0<svg class="spin" viewBox="0 0 5 8"><path d="M0 3.2L2.5 0 5 3.2zM0 4.8L2.5 8 5 4.8z"/></svg></div></div>
    <div class="field"><label>Delivery Discount</label><div class="box box--lg">0</div></div>
  </div>
  <div class="card card--d">
    <div class="field"><label>Status</label><div class="box">New</div></div>
    <div class="field"><label>Location Code</label><div class="box">1301</div></div>
    <div class="field"><label>Customer Email</label><div class="box"></div></div>
    <div class="field"><label>Shipping Tax</label><div class="box">0<svg class="spin" viewBox="0 0 5 8"><path d="M0 3.2L2.5 0 5 3.2zM0 4.8L2.5 8 5 4.8z"/></svg></div></div>
    <div class="field"><label>Created</label><div class="box box--sm">21/01/2022 &nbsp;02:05 PM</div></div>
  </div>

  <div class="tabs">
    <div class="tab">Item</div><div class="tab">Customer(s)</div><div class="tab on">Addresses</div><div class="tab">Payments</div><div class="tab">Vochers</div><div class="tab">Event Queues</div><div class="tab">Updates</div><div class="tab">Fulfilments</div><div class="tab">History</div>
  </div>
  <div class="atable">
    <div class="arow arow--head"><span class="c1">Type</span><span class="c2">Name</span><span class="c3">Attention Of</span><span class="c4">Address</span><span class="c5">Email</span><span class="c6">Phone</span><span class="c7">Actions</span></div>
    <div class="arow arow--lav"><span class="c1">Delivery</span><span class="c2">Test Order</span><span class="c3">-</span><span class="c4">-</span><span class="c5">-</span><span class="c6">-</span><span class="c7">(Edit)</span></div>
    <div class="arow arow--cyan"><span class="c1">Delivery</span><span class="c2">Test Order</span><span class="c3">-</span><span class="c4">-</span><span class="c5">-</span><span class="c6">-</span><span class="c7">(Edit)</span></div>
  </div>

  <div class="dim"></div>
  <div class="modal">
    <div class="modal-head">Address<svg viewBox="0 0 16 16"><circle cx="8" cy="8" r="8" fill="#fff"/><path d="M5 5l6 6M11 5l-6 6" stroke="#33c4c4" stroke-width="2"/></svg></div>
    <div class="form">
      <div class="frow"><label>First name</label><span class="colon">:</span><div class="input">Test</div></div>
      <div class="frow"><label>Surname</label><span class="colon">:</span><div class="input">Order</div></div>
      <div class="frow"><label>Attention of</label><span class="colon">:</span><div class="input"></div></div>
      <div class="frow"><label>Address 1</label><span class="colon">:</span><div class="input"></div></div>
      <div class="frow"><label>Address 2</label><span class="colon">:</span><div class="input"></div></div>
      <div class="frow"><label>Suburb</label><span class="colon">:</span><div class="input"></div></div>
      <div class="frow"><label>City</label><span class="colon">:</span><div class="input"></div></div>
      <div class="frow"><label>State</label><span class="colon">:</span><div class="input"></div></div>
      <div class="frow"><label>Postcode</label><span class="colon">:</span><div class="input"></div></div>
      <div class="frow"><label>Country</label><span class="colon">:</span><div class="input"></div></div>
      <div class="frow"><label>Email</label><span class="colon">:</span><div class="input"></div></div>
      <div class="frow"><label>Phone</label><span class="colon">:</span><div class="input"></div></div>
    </div>
    <div class="actions"><div class="btn btn--update">UPDATE</div><div class="btn btn--cancel">CANCEL</div></div>
  </div>
</section>

<!-- Screen: Item tab -->
<section class="screen screen--items">
  <nav class="side">
    <div class="brand">Order<br>Management</div>
    <ul class="menu">
      <li class="on"><svg class="ic" viewBox="0 0 10 10"><rect x="0" y="1" width="10" height="8" rx="1"/></svg>Dashboard</li>
      <li><svg class="ic" viewBox="0 0 10 10"><circle cx="3" cy="3" r="2"/><circle cx="7" cy="3" r="2"/><rect x="0" y="6" width="10" height="4" rx="2"/></svg>Teams</li>
      <li><svg class="ic" viewBox="0 0 10 10"><path d="M0 1h2l1.5 5h5L10 2.5H3"/><circle cx="4" cy="8.5" r="1"/><circle cx="8" cy="8.5" r="1"/></svg>Cart</li>
      <li><svg class="ic" viewBox="0 0 10 10"><path d="M5 0a3.5 3.5 0 0 1 3.5 3.5C8.5 6 5 10 5 10S1.5 6 1.5 3.5A3.5 3.5 0 0 1 5 0z"/></svg>Location</li>
      <li><svg class="ic" viewBox="0 0 10 10"><ellipse cx="5" cy="5" rx="5" ry="3"/></svg>View</li>
      <li><svg class="ic" viewBox="0 0 10 10"><path d="M5 0l5 5-5 5-5-5z"/></svg>Countries</li>
      <li><svg class="ic" viewBox="0 0 10 10"><circle cx="5" cy="5" r="5"/></svg>Matches</li>
      <li><svg class="ic" viewBox="0 0 10 10"><circle cx="5" cy="5" r="5"/></svg>Questions</li>
      <li><svg class="ic" viewBox="0 0 10 10"><rect x="0" y="1" width="10" height="8" rx="1"/></svg>View Result</li>
      <li><svg class="ic" viewBox="0 0 10 10"><circle cx="5" cy="5" r="4"/></svg>Settings</li>
      <li><svg class="ic" viewBox="0 0 10 10"><path d="M0 4h6V1l4 4-4 4V6H0z"/></svg>Logout</li>
    </ul>
  </nav>
  <h1 class="title">Development</h1>
  <div class="search"><svg viewBox="0 0 10 10"><circle cx="4" cy="4" r="3" fill="none" stroke="#333" stroke-width="1.6"/><path d="M6 6l3 3" stroke="#333" stroke-width="1.6"/></svg>Search...</div>
  <svg class="hicon hicon--mail" viewBox="0 0 10 10"><rect y="1.5" width="10" height="7"/><path d="M0 1.5l5 4 5-4" fill="none" stroke="#fff" stroke-width="1"/></svg>
  <svg class="hicon hicon--bell" viewBox="0 0 10 10"><path d="M5 0.5a3 3 0 0 1 3 3V7l1.5 1.5h-9L2 7V3.5a3 3 0 0 1 3-3z"/><circle cx="5" cy="9.3" r="0.9"/></svg>
  <div class="avatar" role="img" aria-label="User profile photo"></div>
  <div class="hrule"></div>
  <div class="pill">Order Search <svg viewBox="0 0 10 10"><circle cx="5" cy="5" r="5" fill="#fff"/><path d="M3 3l4 4M7 3l-4 4" stroke="#5a44d6" stroke-width="1.4"/></svg></div>
  <div class="crumb">Order 9670363 <svg viewBox="0 0 10 10"><circle cx="5" cy="5" r="4" fill="none" stroke="#3f58c0" stroke-width="2"/></svg></div>

  <div class="card card--a">
    <div class="field"><label>Order No</label><div class="box">9670363</div></div>
    <div class="field"><label>Orig Order No</label><div class="box">9670363</div></div>
    <div class="field"><label>Customer No</label><div class="box"></div></div>
    <div class="field"><label>Total Retail</label><div class="box">102.00<svg class="spin" viewBox="0 0 5 8"><path d="M0 3.2L2.5 0 5 3.2zM0 4.8L2.5 8 5 4.8z"/></svg></div></div>
    <div class="field"><label>Instructions</label><div class="box"></div></div>
  </div>
  <div class="card card--b">
    <div class="field"><label>Brand</label><div class="box"></div></div>
    <div class="field"><label>Reference</label><div class="box">9670363</div></div>
    <div class="field"><label>First name</label><div class="box">Test</div></div>
    <div class="field"><label>Total Tax</label><div class="box">9.55<svg class="spin" viewBox="0 0 5 8"><path d="M0 3.2L2.5 0 5 3.2zM0 4.8L2.5 8 5 4.8z"/></svg></div></div>
    <div class="field"><label></label><div class="box"></div></div>
  </div>
  <div class="card card--c">
    <div class="field"><label>Order Type</label><div class="box">Sale</div></div>
    <div class="field"><label>Order Channel</label><div class="box">Standard</div></div>
    <div class="field"><label>Surname</label><div class="box">Order</div></div>
    <div class="field"><label>Shipping Amount</label><div class="box">0<svg class="spin" viewBox="0 0 5 8"><path d="M0 3.2L2.5 0 5 3.2zM0 4.8L2.5 8 5 4.8z"/></svg></div></div>
    <div class="field"><label>Delivery Discount</label><div class="box box--lg">0</div></div>
  </div>
  <div class="card card--d">
    <div class="field"><label>Status</label><div class="box">New</div></div>
    <div class="field"><label>Location Code</label><div class="box">1301</div></div>
    <div class="field"><label>Customer Email</label><div class="box"></div></div>
    <div class="field"><label>Shipping Tax</label><div class="box">0<svg class="spin" viewBox="0 0 5 8"><path d="M0 3.2L2.5 0 5 3.2zM0 4.8L2.5 8 5 4.8z"/></svg></div></div>
    <div class="field"><label>Created</label><div class="box box--sm">21/01/2022 &nbsp;02:05 PM</div></div>
  </div>

  <div class="tabs">
    <div class="tab on">Item</div><div class="tab">Customer(s)</div><div class="tab">Addresses</div><div class="tab">Payments</div><div class="tab">Vochers</div><div class="tab">Event Queues</div><div class="tab">Updates</div><div class="tab">Fulfilments</div><div class="tab">History</div>
  </div>
  <div class="grid">
    <div class="tr th"><div>SKU</div><div class="span2">PRODUCT</div><div>Is DropShip</div><div>Quantity</div><div>Unit Retail</div><div>Unit Tax</div><div>Discount</div><div>Final</div><div>Discout Reason</div><div>Coupon Code</div><div>Status</div></div>
    <div class="tr td"><div>2230566</div><div class="spec"><span>Vendor</span><span>Brand</span><span>Product Code</span><span>Description</span><span>Colour (Code)</span><span>Size</span></div><div class="spec spec--val"><span>-</span><span>-</span><span>2002569</span><span>PJ SET</span><span>900</span><span>12/14</span></div><div>False</div><div>1</div><div>35.00</div><div>3.18</div><div>0.00</div><div>35.00</div><div></div><div></div><div></div></div>
    <div class="tr td alt"><div>2230566</div><div class="spec"><span>Vendor</span><span>Brand</span><span>Product Code</span><span>Description</span><span>Colour (Code)</span><span>Size</span></div><div class="spec spec--val"><span>-</span><span>-</span><span>2002569</span><span>PJ SET</span><span>900</span><span>12/14</span></div><div>False</div><div>1</div><div>35.00</div><div>3.18</div><div>0.00</div><div>35.00</div><div></div><div></div><div></div></div>
    <div class="tr td"><div>2230568</div><div class="spec"><span>Vendor</span><span>Brand</span><span>Product Code</span><span>Description</span><span>Colour (Code)</span><span>Size</span></div><div class="spec spec--val"><span>-</span><span>-</span><span>2002569</span><span>PJ SET</span><span>900</span><span>12/14</span></div><div>False</div><div>1</div><div>35.00</div><div>3.18</div><div>0.00</div><div>35.00</div><div></div><div></div><div></div></div>
  </div>
</section>

<!-- Screen: Addresses tab -->
<section class="screen screen--addresses">
  <nav class="side">
    <div class="brand">Order<br>Management</div>
    <ul class="menu">
      <li class="on"><svg class="ic" viewBox="0 0 10 10"><rect x="0" y="1" width="10" height="8" rx="1"/></svg>Dashboard</li>
      <li><svg class="ic" viewBox="0 0 10 10"><circle cx="3" cy="3" r="2"/><circle cx="7" cy="3" r="2"/><rect x="0" y="6" width="10" height="4" rx="2"/></svg>Teams</li>
      <li><svg class="ic" viewBox="0 0 10 10"><path d="M0 1h2l1.5 5h5L10 2.5H3"/><circle cx="4" cy="8.5" r="1"/><circle cx="8" cy="8.5" r="1"/></svg>Cart</li>
      <li><svg class="ic" viewBox="0 0 10 10"><path d="M5 0a3.5 3.5 0 0 1 3.5 3.5C8.5 6 5 10 5 10S1.5 6 1.5 3.5A3.5 3.5 0 0 1 5 0z"/></svg>Location</li>
      <li><svg class="ic" viewBox="0 0 10 10"><ellipse cx="5" cy="5" rx="5" ry="3"/></svg>View</li>
      <li><svg class="ic" viewBox="0 0 10 10"><path d="M5 0l5 5-5 5-5-5z"/></svg>Countries</li>
      <li><svg class="ic" viewBox="0 0 10 10"><circle cx="5" cy="5" r="5"/></svg>Matches</li>
      <li><svg class="ic" viewBox="0 0 10 10"><circle cx="5" cy="5" r="5"/></svg>Questions</li>
      <li><svg class="ic" viewBox="0 0 10 10"><rect x="0" y="1" width="10" height="8" rx="1"/></svg>View Result</li>
      <li><svg class="ic" viewBox="0 0 10 10"><circle cx="5" cy="5" r="4"/></svg>Settings</li>
      <li><svg class="ic" viewBox="0 0 10 10"><path d="M0 4h6V1l4 4-4 4V6H0z"/></svg>Logout</li>
    </ul>
  </nav>
  <h1 class="title">Development</h1>
  <div class="search"><svg viewBox="0 0 10 10"><circle cx="4" cy="4" r="3" fill="none" stroke="#333" stroke-width="1.6"/><path d="M6 6l3 3" stroke="#333" stroke-width="1.6"/></svg>Search...</div>
  <svg class="hicon hicon--mail" viewBox="0 0 10 10"><rect y="1.5" width="10" height="7"/><path d="M0 1.5l5 4 5-4" fill="none" stroke="#fff" stroke-width="1"/></svg>
  <svg class="hicon hicon--bell" viewBox="0 0 10 10"><path d="M5 0.5a3 3 0 0 1 3 3V7l1.5 1.5h-9L2 7V3.5a3 3 0 0 1 3-3z"/><circle cx="5" cy="9.3" r="0.9"/></svg>
  <div class="avatar" role="img" aria-label="User profile photo"></div>
  <div class="hrule"></div>
  <div class="pill">Order Search <svg viewBox="0 0 10 10"><circle cx="5" cy="5" r="5" fill="#fff"/><path d="M3 3l4 4M7 3l-4 4" stroke="#5a44d6" stroke-width="1.4"/></svg></div>
  <div class="crumb">Order 9670363 <svg viewBox="0 0 10 10"><circle cx="5" cy="5" r="4" fill="none" stroke="#3f58c0" stroke-width="2"/></svg></div>

  <div class="card card--a">
    <div class="field"><label>Order No</label><div class="box">9670363</div></div>
    <div class="field"><label>Orig Order No</label><div class="box">9670363</div></div>
    <div class="field"><label>Customer No</label><div class="box"></div></div>
    <div class="field"><label>Total Retail</label><div class="box">102.00<svg class="spin" viewBox="0 0 5 8"><path d="M0 3.2L2.5 0 5 3.2zM0 4.8L2.5 8 5 4.8z"/></svg></div></div>
    <div class="field"><label>Instructions</label><div class="box"></div></div>
  </div>
  <div class="card card--b">
    <div class="field"><label>Brand</label><div class="box"></div></div>
    <div class="field"><label>Reference</label><div class="box">9670363</div></div>
    <div class="field"><label>First name</label><div class="box">Test</div></div>
    <div class="field"><label>Total Tax</label><div class="box">9.55<svg class="spin" viewBox="0 0 5 8"><path d="M0 3.2L2.5 0 5 3.2zM0 4.8L2.5 8 5 4.8z"/></svg></div></div>
    <div class="field"><label></label><div class="box"></div></div>
  </div>
  <div class="card card--c">
    <div class="field"><label>Order Type</label><div class="box">Sale</div></div>
    <div class="field"><label>Order Channel</label><div class="box">Standard</div></div>
    <div class="field"><label>Surname</label><div class="box">Order</div></div>
    <div class="field"><label>Shipping Amount</label><div class="box">0<svg class="spin" viewBox="0 0 5 8"><path d="M0 3.2L2.5 0 5 3.2zM0 4.8L2.5 8 5 4.8z"/></svg></div></div>
    <div class="field"><label>Delivery Discount</label><div class="box box--lg">0</div></div>
  </div>
  <div class="card card--d">
    <div class="field"><label>Status</label><div class="box">New</div></div>
    <div class="field"><label>Location Code</label><div class="box">1301</div></div>
    <div class="field"><label>Customer Email</label><div class="box"></div></div>
    <div class="field"><label>Shipping Tax</label><div class="box">0<svg class="spin" viewBox="0 0 5 8"><path d="M0 3.2L2.5 0 5 3.2zM0 4.8L2.5 8 5 4.8z"/></svg></div></div>
    <div class="field"><label>Created</label><div class="box box--sm">21/01/2022 &nbsp;02:05 PM</div></div>
  </div>

  <div class="tabs">
    <div class="tab">Item</div><div class="tab">Customer(s)</div><div class="tab on">Addresses</div><div class="tab">Payments</div><div class="tab">Vochers</div><div class="tab">Event Queues</div><div class="tab">Updates</div><div class="tab">Fulfilments</div><div class="tab">History</div>
  </div>
  <div class="atable">
    <div class="arow arow--head"><span class="c1">Type</span><span class="c2">Name</span><span class="c3">Attention Of</span><span class="c4">Address</span><span class="c5">Email</span><span class="c6">Phone</span><span class="c7">Actions</span></div>
    <div class="arow arow--lav"><span class="c1">Delivery</span><span class="c2">Test Order</span><span class="c3">-</span><span class="c4">-</span><span class="c5">-</span><span class="c6">-</span><span class="c7">(Edit)</span></div>
    <div class="arow arow--cyan"><span class="c1">Delivery</span><span class="c2">Test Order</span><span class="c3">-</span><span class="c4">-</span><span class="c5">-</span><span class="c6">-</span><span class="c7">(Edit)</span></div>
  </div>
</section>

</div>
</body>
</html>
```